Velorik Cement

i need envelope a4 size and normal size - folder -paper bag - business card -
letterhead

Stationery Design project 'Stationery velorik cement : letterhead ,folder,business card ,envelope ,envelope A4size .paper bag '

Target Market(s)

ready mix concrete

Font styles to use
Serif

Colors

Designer to choose colors to be used in the design.

Requirements
Must have
• nice design

```html
<!DOCTYPE html>
<html lang="en">
<head>
<meta charset="utf-8">
<title>Velorik Cement – Stationery</title>
<link rel="stylesheet" href="https://fonts.googleapis.com/css2?family=Source+Serif+4:wght@400;600;700&family=Noto+Naskh+Arabic:wght@400;600&display=swap">
<style>
  :root{
    --navy:#04508a;
    --blue:#0a6fd0;
    --sky:#5ba5cd;
    --sky-soft:#a9d0e6;
    --lilac:#8ea2e0;
    --paper:#ffffff;
    --grey-dark:#8f9094;
    --grey-light:#e6e7e9;
    --ink:#1f1f22;
  }
  *{box-sizing:border-box;margin:0;padding:0}
  html,body{width:1200px;height:1200px;overflow:hidden;background:#fff}
  body{position:relative;font-family:"Source Serif 4",serif;color:var(--navy)}
  .band{position:absolute;left:0;width:1200px;
    background:radial-gradient(ellipse at 50% 50%,var(--grey-light) 0%,#c4c5c8 45%,var(--grey-dark) 100%)}
  .band--top{top:18px;height:454px}
  .band--middle{top:498px;height:454px}
  .band--bottom{top:976px;height:158px}
  .item{position:absolute;box-shadow:2px 3px 6px rgba(0,0,0,.35);overflow:hidden}
  .abs{position:absolute}
  .brand{font-weight:700;color:var(--navy);line-height:1;display:flex;align-items:center;gap:4px}
  .tagline{font-weight:400;text-transform:uppercase;color:var(--navy);line-height:1.2;white-space:nowrap}
  .kurdish{font-family:"Noto Naskh Arabic",serif;direction:rtl;line-height:1.35;white-space:nowrap}
  .kurdish .strong{font-weight:600;color:var(--navy);display:block}
  .kurdish .light{color:#555;display:block}
  .ornament-area{position:absolute}
  /* letterhead */
  .letterhead{left:65px;top:53px;width:263px;height:371px;
    background:linear-gradient(to bottom,var(--lilac) 0%,#fff 40%,#fff 58%,var(--lilac) 100%)}
  .letterhead .contact{right:6px;font-size:5px;font-weight:700;text-align:right;line-height:1.5}
  /* business cards */
  .card-front{left:434px;top:154px;width:152px;height:99px;
    background:linear-gradient(135deg,#3c5fb0 0%,#8d8fd6 50%,#4a78c8 100%)}
  .card-front .contact-list{left:80px;top:36px;font-size:4.5px;color:#fff;font-weight:600;list-style:none}
  .card-front .contact-list li{display:flex;align-items:center;gap:4px;height:12.5px;white-space:nowrap}
  .card-back{left:434px;top:266px;width:153px;height:99px;background:#fff}
  /* folder */
  .folder{left:670px;top:107px;width:456px;height:343px}
  /* envelopes */
  .env-a4-back{left:34px;top:498px;width:371px;height:261px;
    background:linear-gradient(to bottom,var(--lilac) 0%,#fff 30%,#fff 55%,var(--lilac) 100%)}
  .env-a4-front{left:34px;top:770px;width:371px;height:262px;
    background:linear-gradient(to bottom,var(--lilac) 0%,#fff 45%,#fff 100%)}
  .env-small-back{left:475px;top:579px;width:290px;height:150px;transform:rotate(-15deg);
    background:linear-gradient(to bottom,var(--lilac) 0%,#fff 35%,#fff 55%,var(--lilac) 100%)}
  .env-small-front{left:502px;top:746px;width:275px;height:138px;
    background:linear-gradient(to bottom,var(--lilac) 0%,#fff 45%,#fff 100%)}
  .window{position:absolute;background:#fff;border:1px solid #6f8fc4;border-radius:4px}
  .bottom-strip{position:absolute;left:0;bottom:0;width:100%;background:var(--navy)}
  .label{position:absolute;font-family:"Source Sans 3",sans-serif;font-weight:700;color:var(--ink);font-size:27px;letter-spacing:.3px;white-space:nowrap}
  /* bag */
  .bag{left:869px;top:616px;width:289px;height:350px;
    background:linear-gradient(to bottom,var(--lilac) 0%,#fff 45%,#fff 55%,var(--lilac) 100%)}
  .handle{position:absolute;left:930px;top:514px}
</style>
<link rel="stylesheet" href="https://fonts.googleapis.com/css2?family=Source+Sans+3:wght@700&display=swap">
</head>
<body>
  <div class="band band--top"></div>
  <div class="band band--middle"></div>
  <div class="band band--bottom"></div>

  <!-- Letterhead -->
  <section class="item letterhead" aria-label="Letterhead">
    <div class="abs" style="left:11px;top:14px">
      <div class="brand" style="font-size:20px">Velorik</div>
      <div class="tagline" style="font-size:4.5px;margin-top:3px">Velorik for concrete</div>
    </div>
    <div class="abs contact" style="top:50px">velorik@company.com<br>+0198765432</div>
    <div class="ornament-area" role="img" aria-label="Soft blue decorative corner graphic"
      style="left:0;bottom:0;width:80px;height:80px;background:radial-gradient(circle at 10% 100%,rgba(10,111,208,.55) 0%,rgba(169,208,230,.5) 55%,rgba(169,208,230,0) 75%)"></div>
    <div class="abs contact" style="bottom:8px">www.velorik.com<br>street name, city, country</div>
  </section>

  <!-- Business card front -->
  <section class="item card-front" aria-label="Business card, contact side">
    <div class="ornament-area" role="img" aria-label="Soft light decorative band"
      style="left:56px;top:0;width:24px;height:99px;background:linear-gradient(to right,rgba(255,255,255,0),rgba(255,255,255,.45),rgba(255,255,255,0))"></div>
    <div class="abs" style="left:8px;top:38px">
      <div class="brand" style="font-size:13px;color:#fff">Velorik</div>
      <div class="tagline" style="font-size:3.5px;color:#fff;margin-top:2px">Velorik for concrete</div>
    </div>
    <ul class="abs contact-list">
      <li><svg width="5" height="5" viewBox="0 0 10 10"><path d="M2 1l2 0 1 3-1.5 1a6 6 0 0 0 2.5 2.5L7 6l3 1v2C5 10 0 5 1 1z" fill="#fff"/></svg>+0198765432</li>
      <li><svg width="5" height="5" viewBox="0 0 10 10"><rect x="0" y="2" width="10" height="6" fill="#fff"/></svg>velorik@company.com</li>
      <li><svg width="5" height="5" viewBox="0 0 10 10"><rect x="2" y="0" width="6" height="10" rx="1" fill="#fff"/></svg>www.velorik.com</li>
      <li><svg width="5" height="5" viewBox="0 0 10 10"><path d="M5 10L1.5 5A3.5 3.5 0 1 1 8.5 5z" fill="#fff"/></svg>Street Name, City, Country</li>
    </ul>
  </section>

  <!-- Business card back -->
  <section class="item card-back" aria-label="Business card, brand side">
    <div class="abs" style="left:0;width:153px;top:20px;text-align:center">
      <div class="brand" style="font-size:24px;justify-content:center">Velorik</div>
      <div class="tagline" style="font-size:5.5px;margin-top:4px">Velorik for concrete</div>
      <div class="kurdish" style="font-size:6px;margin-top:1px"><span class="strong">کۆمپانیای ڤێلۆریک</span><span class="light">بۆ کۆنکرێتی ئامادەکراو</span></div>
    </div>
  </section>

  <!-- Folder -->
  <section class="folder abs" aria-label="Presentation folder, open flat">
    <svg class="abs" style="left:0;top:0;filter:drop-shadow(2px 3px 3px rgba(0,0,0,.35))" width="456" height="343" viewBox="0 0 456 343">
      <path d="M40 0 L40 293 L0 270 L0 20Z" fill="var(--sky)"/>
      <path d="M40 293 L246 293 L207 343 L40 343Z" fill="var(--sky)"/>
      <rect x="40" y="0" width="207" height="293" fill="var(--navy)"/>
      <rect x="246" y="0" width="210" height="293" fill="var(--sky)"/>
    </svg>
    <div class="abs" style="left:140px;top:216px;width:110px;text-align:center">
      <div class="brand" style="font-size:26px;color:#fff;justify-content:center">Velorik</div>
      <div class="tagline" style="font-size:7px;color:#fff;margin-top:4px">Velorik for concrete</div>
      <div class="kurdish" style="font-size:7.5px;color:#fff"><span class="strong" style="color:#fff">کۆمپانیای ڤێلۆریک</span><span style="display:block">بۆ کۆنکرێتی ئامادەکراو</span></div>
    </div>
    <div class="abs" style="left:260px;top:150px;width:196px;text-align:center">
      <div class="brand" style="font-size:40px;color:var(--sky-soft);justify-content:center">Velorik</div>
      <div class="tagline" style="font-size:11px;color:var(--sky-soft);margin-top:14px">Velorik for concrete</div>
      <div class="kurdish" style="font-size:11px;color:var(--sky-soft)"><span style="display:block;font-weight:600">کۆمپانیای ڤێلۆریک</span><span style="display:block">بۆ کۆنکرێتی ئامادەکراو</span></div>
    </div>
  </section>

  <!-- A4 envelope, back -->
  <section class="item env-a4-back" aria-label="A4 envelope, back"></section>

  <!-- A4 envelope, front -->
  <section class="item env-a4-front" aria-label="A4 envelope, front">
    <svg class="abs" style="left:0;top:0" width="371" height="30" viewBox="0 0 371 30">
      <path d="M0 0 H371 L350 26 H20Z" fill="var(--navy)"/>
    </svg>
    <div class="window" style="left:28px;top:93px;width:168px;height:76px;border-radius:6px"></div>
    <div class="abs" style="left:256px;top:92px;width:110px;text-align:center">
      <div class="brand" style="font-size:30px;justify-content:center">Velorik</div>
      <div class="tagline" style="font-size:7px;margin-top:5px">Velorik for concrete</div>
      <div class="kurdish" style="font-size:8px"><span class="strong">کۆمپانیای ڤێلۆریک</span><span class="light">بۆ کۆنکرێتی ئامادەکراو</span></div>
    </div>
    <div class="bottom-strip" style="height:20px"></div>
  </section>

  <!-- Normal envelope, back -->
  <section class="item env-small-back" aria-label="Standard envelope, back"></section>

  <!-- Normal envelope, front -->
  <section class="item env-small-front" aria-label="Standard envelope, front">
    <svg class="abs" style="left:0;top:0" width="275" height="28" viewBox="0 0 275 28">
      <path d="M0 0 H275 L262 27 H13Z" fill="var(--navy)"/>
    </svg>
    <div class="window" style="left:24px;top:65px;width:86px;height:38px;border-radius:3px"></div>
    <div class="abs" style="left:195px;top:54px;width:70px;text-align:center">
      <div class="brand" style="font-size:17px;justify-content:center">Velorik</div>
      <div class="tagline" style="font-size:4.5px;margin-top:3px">Velorik for concrete</div>
      <div class="kurdish" style="font-size:5px"><span class="strong">کۆمپانیای ڤێلۆریک</span><span class="light">بۆ کۆنکرێتی ئامادەکراو</span></div>
    </div>
    <div class="bottom-strip" style="height:8px"></div>
  </section>

  <div class="label" style="left:506px;top:914px">envelope normal size</div>
  <div class="label" style="left:92px;top:1057px">envelope A4 size</div>

  <!-- Paper bag -->
  <svg class="handle" width="150" height="104" viewBox="0 0 150 104" aria-hidden="true">
    <path d="M8 104 C-4 40 30 2 75 2 C120 2 154 40 142 104" fill="none" stroke="#b39a6e" stroke-width="3"/>
    <path d="M14 104 C4 46 34 8 75 8 C116 8 146 46 136 104" fill="none" stroke="#8c7650" stroke-width="2"/>
  </svg>
  <section class="item bag" aria-label="Paper bag">
    <div class="ornament-area" role="img" aria-label="Soft blue decorative corner graphic"
      style="left:0;bottom:0;width:160px;height:180px;background:radial-gradient(circle at 12% 100%,rgba(10,111,208,.55) 0%,rgba(91,165,205,.4) 50%,rgba(255,255,255,0) 78%)"></div>
    <div class="abs" style="left:145px;top:230px;width:130px;text-align:center">
      <div class="brand" style="font-size:34px;justify-content:center">Velorik</div>
      <div class="tagline" style="font-size:8.5px;margin-top:6px">Velorik for concrete</div>
    </div>
  </section>
</body>
</html>
```